Etiketten für Wein und Sekt
Zielgruppe
Sekt- und Weinherstellung
Zielgruppe 25 - 60 Jahre
Aufgabenstellung
Wir führen ein neues Produkt in den Markt ein:
gewünschter Name: The Velvet Orchard Taste
Hervorgehoben werden soll 'Velvet Orchard'
auf dieser Basis suchern wir einmal das Etikett für den WEIN
und einmal das Etikett für den SEKT (gleiches Design/Designfamilie)
Beim Sekt dachten wir an den Zusatz Sparkling auf dem Etikett?
Achtung, es handelt sich hier um keinen Eiswein !
Damit darf unser Produkt nicht in Verbindung gebracht werden (dt. Weinrecht)
Unser Wein/Sekt ist ein fruchtiger Rose Wein/Sekt
Ein Cuvée aus regionalen Rebsorten
Beim Trinkgenuss sollen die Gedanken an gefrorene Beeren/Trauben gehen.
Wir dachten an Beerentöne und Rosegold (wie der Inhalt)
Aktuell verwenden wir Etikettenformen in Rechteckgröße horizontal oder vertikal
Besten Dank im Voraus !!

```html
<!DOCTYPE html>
<html lang="de">
<head>
<meta charset="utf-8">
<title>The Velvet Orchard Taste – Sparkling</title>
<link rel="stylesheet" href="https://fonts.googleapis.com/css2?family=Open+Sans:wght@400;600&display=swap">
<style>
  :root {
    --berry-dark: #2a2238;
    --berry-plum: #4a3552;
    --berry-red: #b8334f;
    --berry-rose: #d9667e;
    --frost: #8c7f96;
    --title-color: #f3d6f0;
    --caption: #ffffff;
  }
  * { margin: 0; padding: 0; box-sizing: border-box; }
  html, body {
    width: 963px;
    height: 1200px;
    overflow: hidden;
    background: var(--berry-dark);
  }
  .label {
    position: relative;
    width: 963px;
    height: 1200px;
    overflow: hidden;
    font-family: "Open Sans", sans-serif;
  }
  .label__photo {
    position: absolute;
    inset: 0;
    background:
      radial-gradient(circle at 22% 18%, var(--frost) 0, rgba(140,127,150,0) 22%),
      radial-gradient(circle at 62% 14%, var(--berry-rose) 0, rgba(217,102,126,0) 22%),
      radial-gradient(circle at 92% 48%, var(--berry-rose) 0, rgba(217,102,126,0) 18%),
      radial-gradient(circle at 14% 78%, var(--berry-rose) 0, rgba(217,102,126,0) 20%),
      radial-gradient(circle at 60% 92%, var(--berry-red) 0, rgba(184,51,79,0) 22%),
      radial-gradient(circle at 40% 55%, var(--berry-red) 0, rgba(184,51,79,0) 26%),
      radial-gradient(circle at 80% 80%, var(--berry-plum) 0, rgba(74,53,82,0) 30%),
      linear-gradient(160deg, var(--berry-plum), var(--berry-dark));
  }
  .label__title {
    position: absolute;
    inset: 0;
    font-weight: 600;
    color: var(--title-color);
    text-align: center;
    line-height: 1;
  }
  .label__title span {
    position: absolute;
    left: 0;
    right: 0;
    display: block;
  }
  .label__title-small { top: 275px; font-size: 96px; }
  .label__title-main  { top: 455px; font-size: 108px; letter-spacing: -1px; }
  .label__title-tail  { top: 615px; font-size: 96px; }
  .label__variant {
    position: absolute;
    left: 0; right: 0;
    top: 985px;
    text-align: center;
    font-size: 62px;
    font-weight: 400;
    color: var(--caption);
    line-height: 1;
  }
  .label__blend {
    position: absolute;
    left: 0; right: 0;
    top: 1120px;
    text-align: center;
    font-size: 44px;
    font-weight: 400;
    color: var(--caption);
    line-height: 1;
  }
</style>
</head>
<body>
  <main class="label">
    <div class="label__photo" role="img" aria-label="Close-up photograph of frosted frozen raspberries and blackberries"></div>
    <h1 class="label__title">
      <span class="label__title-small">The</span>
      <span class="label__title-main">Velvet Orchard</span>
      <span class="label__title-tail">Taste</span>
    </h1>
    <p class="label__variant">Sparkling</p>
    <p class="label__blend">Cuvée aus regionalen Rebsorten</p>
  </main>
</body>
</html>
```